Glow & Fizz Soiree for an Aesthetic practice

Please highlight creatively our event on 12/12/18 10AM-7PM at 8198 Jog RD Suite 104Boynton Beach FL 33419
RSVP at (561)-732-4085
*Velumyx Special $10 a unit (Bank your Velumyx for future treatments)
*20% off individual treatments or any DERMAVELLE products
*30% off package purchases
*Twice Sparkle- buy a gift card receive DOUBLE the amount up to $200
*Can't make it on 12/12/18- Call to schedule your appointment and prepay to lock in SPECIAL pricing
*Refer just 2 people or bring them as guests receive $100 worth of services or products FREE!!
* Food and Drinks
*Raffles
*Gift Bags
*Dermavelle Demos
Please use color scheme shown in Logo below
modern and feminine

Target Market(s)

Women and Men 25-65

Requirements
Must have
• R.O.E. Medical Weight Loss & Aesthetics
• address aand time above
Nice to have
• bubbles with specials inside

```html
<!DOCTYPE html>
<html lang="en">
<head>
<meta charset="utf-8">
<title>Glow &amp; Fizz Soiree – R.O.E. Medical Weight Loss &amp; Aesthetics</title>
<link href="https://fonts.googleapis.com/css2?family=Lato:ital,wght@0,400;0,700;0,900;1,400;1,700&family=Oswald:wght@300;400;500;600&display=swap" rel="stylesheet">
<style>
  :root {
    --teal: #34b4bf;
    --teal-deep: #1f8f99;
    --teal-pale: #c8eef2;
    --slate: #3b4657;
    --slate-dark: #2a3443;
    --navy: #1e2a3a;
    --silver: #dfe3e8;
    --white: #ffffff;
  }
  html, body { margin: 0; padding: 0; overflow: hidden; }
  body { width: 902px; height: 1200px; background: var(--white); font-family: "Lato", sans-serif; }
  .flyer { position: relative; width: 902px; height: 1200px; overflow: hidden; background: var(--white); }
  .flyer__shapes { position: absolute; inset: 0; }
  .abs { position: absolute; }

  .brand { left: 88px; top: 120px; color: var(--silver); }
  .brand__name { font-family: "Lato", sans-serif; font-weight: 400; font-size: 118px; letter-spacing: 6px; line-height: 1; margin: 0; }
  .brand__tagline { margin: 8px 0 0 200px; font-size: 13px; line-height: 1.25; letter-spacing: .5px; text-transform: uppercase; color: var(--silver); }

  .badge { left: 511px; top: 24px; width: 360px; height: 380px; text-align: center; color: var(--navy); }
  .badge__lead { position: absolute; top: 74px; left: 0; right: 0; font-family: "Oswald", sans-serif; font-weight: 300; font-size: 38px; line-height: 40px; letter-spacing: 1px; }
  .badge__date { position: absolute; top: 168px; left: 0; right: 0; font-family: "Oswald", sans-serif; font-weight: 500; font-size: 35px; line-height: 44px; }
  .badge__date sup { font-size: 16px; }
  .badge__time { position: absolute; top: 239px; left: 0; right: 0; font-family: "Oswald", sans-serif; font-weight: 400; font-size: 24px; line-height: 28px; }
  .badge__address { position: absolute; top: 283px; left: 0; right: 0; font-weight: 700; font-size: 19px; line-height: 24px; }

  .special { left: 476px; top: 430px; font-family: "Oswald", sans-serif; font-weight: 600; font-size: 29px; color: var(--white); line-height: 56px; white-space: nowrap; }
  .special span { color: var(--navy); }
  .price { left: 712px; top: 432px; width: 150px; height: 54px; background: var(--white); border: 3px solid var(--navy); border-radius: 6px; box-sizing: border-box; font-family: "Oswald", sans-serif; color: var(--navy); font-weight: 600; font-size: 38px; line-height: 48px; text-align: center; }
  .price small { font-size: 22px; }
  .price-note { left: 474px; top: 492px; width: 386px; height: 36px; background: var(--slate-dark); color: var(--white); font-style: italic; font-weight: 700; font-size: 18px; line-height: 36px; text-align: center; }

  .offer { border: 2px dashed rgba(255,255,255,.85); border-radius: 14px; display: flex; align-items: center; color: var(--white); font-family: "Oswald", sans-serif; box-sizing: border-box; }
  .offer__pct { font-weight: 500; font-size: 72px; line-height: 1; }
  .offer__off { writing-mode: vertical-rl; transform: rotate(180deg); font-weight: 600; font-size: 26px; line-height: 1; margin: 0 8px 0 4px; letter-spacing: 1px; }
  .offer__text { font-size: 20px; line-height: 27px; text-transform: uppercase; }
  .offer--twenty { left: 466px; top: 560px; width: 416px; height: 106px; padding-left: 12px; }
  .offer--thirty { left: 510px; top: 684px; width: 306px; height: 104px; padding-left: 18px; }

  .sparkle-title { left: 503px; top: 818px; width: 399px; text-align: center; color: var(--white); font-weight: 700; font-size: 19px; letter-spacing: .5px; }
  .sparkle-bar { left: 503px; top: 852px; width: 399px; height: 64px; background: var(--slate); color: var(--white); font-style: italic; font-size: 19px; line-height: 26px; text-align: center; display: flex; align-items: center; justify-content: center; }

  .alt-date { left: 40px; top: 755px; width: 400px; text-align: center; color: var(--navy); }
  .alt-date__head { font-style: italic; font-weight: 700; color: var(--teal-deep); font-size: 29px; line-height: 34px; }
  .alt-date__date { font-style: italic; font-weight: 700; font-size: 29px; line-height: 34px; }
  .alt-date__date sup { font-size: 16px; }
  .alt-date__body { font-weight: 700; font-size: 20px; line-height: 28px; margin-top: 4px; }

  .referral { left: 0; top: 925px; width: 514px; height: 88px; background: var(--slate); box-sizing: border-box; padding: 14px 0 0 34px; font-style: italic; font-weight: 700; font-size: 18px; line-height: 25px; color: var(--white); }
  .referral em { color: var(--teal); font-style: italic; }

  .perks { left: 636px; top: 964px; margin: 0; padding: 0; list-style: none; }
  .perks li { position: relative; padding-left: 36px; font-style: italic; font-weight: 700; font-size: 22px; line-height: 36px; color: var(--navy); }
  .perks li::before { content: ""; position: absolute; left: 0; top: 9px; width: 18px; height: 18px; border-radius: 50%; background: var(--teal); }

  .follow { left: 54px; top: 1040px; display: flex; align-items: center; gap: 12px; font-style: italic; font-weight: 700; font-size: 19px; color: var(--navy); }
  .follow__dot { width: 32px; height: 32px; border-radius: 50%; background: var(--navy); }

  .rsvp { left: 70px; top: 1118px; font-weight: 900; font-size: 33px; color: var(--navy); }
  .rsvp span { color: var(--white); }
</style>
</head>
<body>
<main class="flyer">
  <svg class="flyer__shapes" width="902" height="1200" viewBox="0 0 902 1200" aria-hidden="true">
    <defs>
      <linearGradient id="header-fill" x1="0" y1="0" x2="1" y2="1">
        <stop offset="0" stop-color="#56627a"/>
        <stop offset="1" stop-color="#2b3442"/>
      </linearGradient>
      <linearGradient id="ring-fill" x1="0" y1="0" x2="1" y2="1">
        <stop offset="0" stop-color="#f4f6f8"/>
        <stop offset=".5" stop-color="#9aa3ad"/>
        <stop offset="1" stop-color="#e6e9ec"/>
      </linearGradient>
      <linearGradient id="badge-top" x1="0" y1="0" x2="0" y2="1">
        <stop offset="0" stop-color="#e3f6f8"/>
        <stop offset="1" stop-color="#7ed5dd"/>
      </linearGradient>
      <clipPath id="badge-clip"><circle cx="691" cy="214" r="172"/></clipPath>
    </defs>

    <!-- teal offers panel -->
    <path d="M902 250 V852 H503 C450 740 430 560 468 360 C560 330 760 300 902 250 Z" fill="var(--teal)"/>
    <!-- header band with teal edge -->
    <path d="M0 0 H902 V296 C700 308 470 340 310 398 C200 438 90 446 0 430 Z" fill="var(--teal)"/>
    <path d="M0 0 H902 V280 C700 292 470 322 300 382 C195 420 90 428 0 414 Z" fill="url(#header-fill)"/>

    <!-- event badge -->
    <circle cx="691" cy="214" r="190" fill="url(#ring-fill)"/>
    <circle cx="691" cy="214" r="177" fill="#4b5563"/>
    <g clip-path="url(#badge-clip)">
      <rect x="510" y="30" width="362" height="160" fill="url(#badge-top)"/>
      <rect x="510" y="190" width="362" height="50" fill="var(--white)"/>
      <rect x="510" y="240" width="362" height="36" fill="var(--teal-pale)"/>
      <rect x="510" y="276" width="362" height="130" fill="#7ed5dd"/>
    </g>

    <!-- treatment photo -->
    <circle cx="225" cy="577" r="168" fill="none" stroke="var(--teal)" stroke-width="7"/>
    <circle cx="225" cy="577" r="158" fill="#d9c2b0" role="img" aria-label="Photo of a woman receiving a cosmetic injection treatment"/>

    <!-- referral icon -->
    <circle cx="545" cy="975" r="44" fill="var(--white)" stroke="var(--teal)" stroke-width="6"/>
    <g fill="var(--navy)">
      <circle cx="531" cy="955" r="7"/><circle cx="559" cy="955" r="7"/>
      <rect x="521" y="965" width="20" height="30" rx="6"/><rect x="549" y="965" width="20" height="30" rx="6"/>
    </g>
    <circle cx="545" cy="978" r="9" fill="var(--white)"/>
    <path d="M540 978 H550 M546 974 L550 978 L546 982" stroke="var(--navy)" stroke-width="2.5" fill="none"/>

    <!-- footer waves -->
    <path d="M400 1080 C560 1090 680 1140 740 1200 H712 C650 1150 540 1102 400 1092 Z" fill="var(--slate)"/>
    <path d="M0 1110 C200 1075 440 1080 560 1110 C630 1130 680 1165 712 1200 H0 Z" fill="var(--teal)"/>
  </svg>

  <header class="brand abs">
    <h1 class="brand__name">R.O.E.</h1>
    <p class="brand__tagline">Medical Weight Loss<br>&amp; Aesthetics</p>
  </header>

  <section class="badge abs">
    <div class="badge__lead">ATTEND OUR<br>EVENT ON</div>
    <div class="badge__date">12<sup>TH</sup> DECEMBER, 2018</div>
    <div class="badge__time">10AM-7PM</div>
    <div class="badge__address">4527 Marlow RD Suite<br>208Boynton Beach<br>FL 33419</div>
  </section>

  <div class="special abs">VELUMYX <span>SPECIAL</span></div>
  <div class="price abs">$10/<small>UNIT</small></div>
  <div class="price-note abs">(Bank your Velumyx for future treatments)</div>

  <div class="offer offer--twenty abs">
    <span class="offer__pct">20%</span><span class="offer__off">OFF</span>
    <span class="offer__text">Individual treatments or<br>any Dermavelle products</span>
  </div>
  <div class="offer offer--thirty abs">
    <span class="offer__pct">30%</span><span class="offer__off">OFF</span>
    <span class="offer__text">Package<br>purchases</span>
  </div>

  <div class="sparkle-title abs">TWICE SPARKLE</div>
  <div class="sparkle-bar abs">Buy a gift card receive DOUBLE the<br>amount up to $200</div>

  <section class="alt-date abs">
    <div class="alt-date__head">Can't make it on</div>
    <div class="alt-date__date">12<sup>th</sup> December, 2018</div>
    <div class="alt-date__body">Call to schedule your appointment<br>and prepay to lock in<br>SPECIAL pricing</div>
  </section>

  <div class="referral abs">Refer just 2 people or bring them as guests<br><em>receive $100 worth of services or products FREE!!</em></div>

  <ul class="perks abs">
    <li>Food and Drinks</li>
    <li>Raffles</li>
    <li>Gift Bags</li>
    <li>Dermavelle Demos</li>
  </ul>

  <div class="follow abs">Follow us on <span class="follow__dot"></span><span class="follow__dot"></span><span class="follow__dot"></span></div>

  <div class="rsvp abs">RSVP at <span>(561)-732-4085</span></div>
</main>
</body>
</html>
```